Business card design needed

The company name is Wendale Architects. We are an architectural company based in Melbourne,Australia that has a mix of client base from health care, commercial office, aged care, multi-residential, single residential and retail. Design type is contemporary.

Suggest the base colours need to be black and white. Please leave an area on the back of the card available for handwritten notes.

Target Market(s)

Generally corporate, aged 30 to 65

Industry/Entity Type

Residential

Contact Information for Business Card

Wendale Architects
Mark Wendale
14 Pellow Street
Rosevale VIC 3071
T (03) 9512 4067
M 0438 617 295
E mw@wendalearc.com.au

Logo Text

WA

Logo styles of interest
Emblem Logo
Abstract Logo
Lettermark Logo
Requirements
Must have
• I am having trouble attaching a sketch so would really appreciate your effort to try the following brief.

Black and White (B&W)
Would like different card cutout profile. Logo Example, use the half circle curve of the G to form the left edge of the card with no margin. The A is to sit inside the G, connected to the G by its horizontal. The A has its cross bar and lower right leg removed. Card in black, text in white.

Back of card to be black text on white background with services provided.

Client Focused Service
Architecture and Design
Functional Planning
Town Planning
Feasability Studies
Contract Documentation
Contract Administration
Project Management

Simple elegant text, Ariel or similar
Nice to have
• Integrated logo and card cut-out.

Card base black on front, white on back
Should not have
• Too many colours
Fussy details

```html
<!DOCTYPE html>
<html lang="en">
<head>
<meta charset="utf-8">
<title>Wendale Architects – Business Card</title>
<link rel="stylesheet" href="https://fonts.googleapis.com/css2?family=Arimo&family=Tinos&display=swap">
<style>
  :root {
    --backdrop: #cfc9bf;
    --card-black: #2b2b2b;
    --card-black-deep: #1f1f1f;
    --card-white: #ffffff;
    --ink: #111111;
    --paper-text: #f4f4f4;
    --shadow: rgba(0, 0, 0, 0.28);
  }
  * { box-sizing: border-box; margin: 0; padding: 0; }
  html, body {
    width: 1200px;
    height: 800px;
    overflow: hidden;
    background: var(--backdrop);
  }
  .stage {
    position: relative;
    width: 1200px;
    height: 800px;
  }
  .card {
    position: absolute;
    top: 100px;
    width: 330px;
    height: 600px;
    border-radius: 165px 165px 0 0;
    box-shadow: 0 14px 30px var(--shadow);
    overflow: hidden;
  }
  .card--front {
    left: 200px;
    background: linear-gradient(160deg, var(--card-black), var(--card-black-deep));
    color: var(--paper-text);
    font-family: "Tinos", "Times New Roman", serif;
  }
  .card--back {
    left: 670px;
    background: var(--card-white);
    color: var(--ink);
    font-family: "Arimo", Arial, sans-serif;
  }

  /* Front */
  .brand__mark {
    position: absolute;
    left: 115px;
    top: 55px;
    width: 100px;
    height: 100px;
    border-radius: 50%;
    background: var(--paper-text);
  }
  .brand__name {
    position: absolute;
    left: 34px;
    top: 185px;
    writing-mode: vertical-rl;
    font-size: 34px;
    line-height: 44px;
    letter-spacing: 8px;
    text-transform: uppercase;
  }
  .contact {
    position: absolute;
    right: 34px;
    top: 250px;
    writing-mode: vertical-rl;
  }
  .contact__name {
    font-size: 32px;
    letter-spacing: 2px;
    margin-left: 16px;
  }
  .contact__line {
    font-size: 15px;
    line-height: 22px;
    letter-spacing: 0.5px;
  }

  /* Back */
  .services {
    position: absolute;
    right: 34px;
    top: 170px;
    writing-mode: vertical-rl;
  }
  .services__title {
    font-size: 26px;
    font-weight: 400;
    margin-left: 14px;
  }
  .services__list {
    list-style: none;
  }
  .services__item {
    font-size: 20px;
    line-height: 26px;
    display: flex;
    align-items: center;
    gap: 8px;
  }
  .services__item::before {
    content: "";
    width: 13px;
    height: 13px;
    border-radius: 50%;
    background: var(--ink);
  }
</style>
</head>
<body>
<main class="stage">
  <section class="card card--front" aria-label="Card front">
    <span class="brand__mark" aria-hidden="true"></span>
    <p class="brand__name">Wendale<br>Architects</p>
    <div class="contact">
      <p class="contact__name">Mark Wendale</p>
      <p class="contact__line">14 Pellow Street</p>
      <p class="contact__line">Rosevale VIC 3071</p>
      <p class="contact__line">T (03) 9512 4067</p>
      <p class="contact__line">M 0438 617 295</p>
      <p class="contact__line">E mw@wendalearc.com.au</p>
    </div>
  </section>

  <section class="card card--back" aria-label="Card back">
    <div class="services">
      <h2 class="services__title">Client Focused Service</h2>
      <ul class="services__list">
        <li class="services__item">Client Focused Service</li>
        <li class="services__item">Architecture and Design</li>
        <li class="services__item">Functional Planning</li>
        <li class="services__item">Town Planning</li>
        <li class="services__item">Feasability Studies</li>
        <li class="services__item">Contract Documentation</li>
        <li class="services__item">Contract Administration</li>
        <li class="services__item">Project Management</li>
      </ul>
    </div>
  </section>
</main>
</body>
</html>
```